TuneNest - Music Industry App needs a top quality wordpress homepage

We need a modern responsive wordpress homepage built. Our website will only feature one page with the goal to get people to sign up to our app. A word document has been uploaded outlining the page content/sections.

Once the homepage is finalised, I will also need 2 landing pages built as part of this competition. It will be very similar to the homepage with the same layout etc but just feature different images and content. The homepage is for anyone (artists and venues) to find out about us but the landing pages will be artist or venue specific.

The completed work must be delivered as an exportable file into wordpress and be designed properly so no more work is needed to begin utilising as the actual website. The images used must be setup correctly for speed and quality also.

Target Market(s)

Venues and Artists.

Coding

Coded - Design and coding required

Requirements
Must have
• UPDATE: High Res Logo files attached
• Must be a modern looking website and be responsive. Must look good across all devices from desktop, to mobile and tablet. Needs to be very high quality.
• Please see the attached logo - I am waiting for the final high quality version and will reupload when complete but this will be enough to get you started for now. The website must have a dark base colour and have red/white elements to match the logo. The red colour used MUST match the red colour used in the logo.
• Please have a go at creating it how you think is best and provide feedback from there. I am leaving it very open to the designers so I can get the best website possible and lots of different ideas etc.

```html
<!DOCTYPE html>
<html lang="en">
<head>
<meta charset="utf-8">
<title>TuneNest – Rovr for Live Music</title>
<link rel="stylesheet" href="https://fonts.googleapis.com/css2?family=Anton&family=Teko:wght@400;500;600&family=Montserrat:ital,wght@0,400;0,500;0,600;0,700;1,400&display=swap">
<style>
:root{
  --red:#e1061a;
  --dark:#05040f;
  --black:#000;
  --white:#fff;
  --card:#f5f5f5;
  --ink:#2a2a2a;
  --muted:#777;
  --green:#1cc21a;
  --navy:#0b1538;
  --line:#bbb;
}
*{box-sizing:border-box;margin:0;padding:0}
html,body{width:1200px;height:3717px;overflow:hidden}
body{position:relative;background:var(--dark);font-family:"Montserrat",sans-serif;color:var(--white)}
.abs{position:absolute}

/* hero */
.hero{left:0;top:0;width:1200px;height:551px;overflow:hidden}
.hero-photo{position:absolute;inset:0;background:
  radial-gradient(ellipse at 70% 20%,#6a3be0 0%,transparent 55%),
  radial-gradient(ellipse at 20% 10%,#5a2ad0 0%,transparent 50%),
  linear-gradient(180deg,#3d1ba8 0%,#2a1275 55%,#0d0620 100%)}
.brand{display:flex;align-items:center;gap:8px;font-family:"Montserrat",sans-serif;font-weight:500;color:var(--white)}
.brand-dot{width:14px;height:14px;border-radius:50%;background:var(--red)}
.hero .brand{left:0;width:1200px;top:48px;justify-content:center;font-size:30px}
.hero-title{left:0;width:1200px;top:140px;text-align:center;font-family:"Anton",sans-serif;font-size:100px;line-height:94px;letter-spacing:1px;text-transform:uppercase}
.hero-sub{left:0;width:1200px;top:346px;text-align:center;font-size:17px;font-weight:500}
.hero-cta{left:326px;top:420px;display:flex;align-items:center}
.hero-cta .lead{font-size:23px;font-weight:500;margin-right:16px;width:232px}
.hero-cta .lead b{color:#6fc4ff;font-weight:600}
.signup{display:flex;height:36px}
.signup input{border:1px solid #ddd;background:var(--white);font-family:inherit;font-size:11px;padding:0 12px;color:var(--muted)}
.signup button{border:0;background:var(--green);color:var(--white);font-family:inherit;font-size:11px;font-weight:700;text-transform:uppercase}

/* how it works */
.how-title{left:187px;top:628px;font-family:"Teko",sans-serif;font-weight:500;font-size:76px;line-height:1}
.step-num{top:738px;font-family:"Teko",sans-serif;font-weight:500;font-size:50px;line-height:1}
.step-line{left:220px;top:825px;width:663px;height:2px;background:#ddd}
.step-dot{top:812px;width:28px;height:28px;border-radius:50%;background:var(--red);display:flex;align-items:center;justify-content:center}
.step-card{top:867px;width:141px;background:var(--card);color:var(--ink);font-size:12.5px;line-height:19.5px;padding:22px 22px 12px 24px}
.step-card::before{content:"";position:absolute;left:14px;top:-9px;border:9px solid transparent;border-top:0;border-bottom-color:var(--card)}

/* why */
.why-bg{left:0;top:1126px;width:1200px;height:1268px}
.why-title{left:0;width:1200px;top:1205px;text-align:center;font-family:"Teko",sans-serif;font-weight:500;font-size:80px;line-height:1}
.why-panel{left:159px;top:1288px;width:885px;height:353px;background:rgba(0,0,0,.07);box-shadow:0 10px 30px rgba(0,0,0,.25)}
.why-core{left:456px;top:1321px;width:288px;height:288px;border-radius:50%;background:var(--black);display:flex;align-items:center;justify-content:center;box-shadow:0 6px 30px rgba(0,0,0,.45)}
.why-core .brand{font-size:40px}
.why-core .brand-dot{width:20px;height:20px}
.feature-icon{width:96px;height:96px;border-radius:50%;background:var(--red);border:5px solid var(--white);display:flex;align-items:center;justify-content:center}
.feature h3{font-size:17px;font-weight:600;text-transform:uppercase;margin-bottom:6px}
.feature p{font-size:12.5px;line-height:19px}
.feature.right-al{text-align:right}

/* venues & artists */
.block-title{font-family:"Teko",sans-serif;font-weight:500;font-size:76px;line-height:1;text-align:center}
.venues{left:193px;top:1708px;width:370px}
.artists-card{left:600px;top:1681px;width:444px;height:668px;background:var(--white);color:var(--ink)}
.artists{left:39px;top:27px;width:368px}
.perks{list-style:none;margin-top:22px}
.perks li{position:relative;padding-left:32px;font-size:12.5px;line-height:20px;margin-bottom:15px}
.perks li::before{content:"";position:absolute;left:13px;top:6px;width:7px;height:7px;border-radius:50%;background:currentColor}
.note{font-size:12.3px;font-style:italic;line-height:22.5px;margin-top:-6px}
.form-lead{font-size:23px;line-height:23px;font-weight:500;text-align:center;margin:40px 0 12px}
.venues .signup{height:34px}
.venues .signup input{width:220px}
.venues .signup button{width:148px}
.artists .form-lead{margin:18px 0 8px}
.artists .signup input{width:244px;border-color:#e3e3e3}
.artists .signup button{width:122px}

/* about */
.about-photo{left:0;top:2448px;width:1200px;height:678px;background:
  radial-gradient(ellipse at 50% 95%,#ff5a1f 0%,transparent 45%),
  radial-gradient(ellipse at 20% 90%,#c23a12 0%,transparent 40%),
  linear-gradient(180deg,#0c0a1f 0%,#1c1533 25%,#2a1526 55%,#6b1e0e 85%,#9a2a0c 100%)}
.about-band{left:0;top:2595px;width:1200px;height:531px;background:rgba(30,25,60,.35)}
.about-title{left:0;width:1200px;top:2532px;text-align:center;font-family:"Teko",sans-serif;font-weight:500;font-size:76px;line-height:1}
.about-col{top:2683px;width:365px}
.about-col h3{font-family:"Teko",sans-serif;font-weight:500;font-size:54px;line-height:1;text-align:center}
.about-col h3::after{content:"";display:block;width:14px;height:2px;background:var(--white);margin:8px auto 16px}
.about-col p{font-size:13px;line-height:22.5px;margin-bottom:28px}

/* contact */
.contact{left:0;top:3126px;width:1200px;height:511px;background:var(--white)}
.contact-title{left:186px;top:108px;color:var(--ink);font-size:48px;font-weight:400;line-height:1}
.contact-title::after{content:"";display:block;width:46px;height:2px;background:var(--red);margin-top:10px}
.field{border:0;border-bottom:1px solid var(--line);background:transparent;font-family:inherit;font-size:11px;color:var(--muted);padding:0 12px 6px;height:22px}
.field::placeholder,.signup input::placeholder{color:#999}
textarea.field{resize:none;height:76px;padding-top:0}
.send{left:414px;top:365px;width:154px;height:34px;border:0;background:var(--black);color:var(--white);font-family:inherit;font-size:11px;font-weight:600;text-transform:uppercase}
.contact-card{left:600px;top:78px;width:444px;height:352px;background:var(--black);text-align:center}
.contact-card .phone{position:absolute;left:0;width:444px;top:133px;font-size:26px;font-weight:500}
.contact-card .info{position:absolute;left:0;width:444px;font-size:11.5px}
.contact-card .info b{font-weight:700}

.footer{left:0;top:3637px;width:1200px;height:80px;background:var(--navy);text-align:center;font-size:11px;line-height:80px}
</style>
</head>
<body>

<header class="abs hero">
  <div class="hero-photo" role="img" aria-label="Concert crowd with raised hands under purple stage lights"></div>
  <div class="abs brand"><span class="brand-dot"></span>TuneNest</div>
  <h1 class="abs hero-title">Rovr for<br>live music</h1>
  <p class="abs hero-sub">TuneNest connects venues with artists to make booking gigs simple</p>
  <div class="abs hero-cta">
    <span class="lead">Sign up now for <b>FREE</b></span>
    <form class="signup"><input type="email" placeholder="Email" style="width:199px"><button type="button" style="width:99px">Sign up</button></form>
  </div>
</header>

<section class="how">
  <h2 class="abs how-title">How TuneNest Works</h2>
  <span class="abs step-num" style="left:204px">1</span>
  <span class="abs step-num" style="left:370px">2</span>
  <span class="abs step-num" style="left:535px">3</span>
  <span class="abs step-num" style="left:701px">4</span>
  <span class="abs step-num" style="left:866px">5</span>
  <div class="abs step-line"></div>
  <div class="abs step-dot" style="left:206px"><svg width="12" height="12" viewBox="0 0 12 12" fill="#fff"><circle cx="6" cy="3.5" r="2.5"/><path d="M1 12c0-3 2.2-5 5-5s5 2 5 5z"/></svg></div>
  <div class="abs step-dot" style="left:372px"><svg width="12" height="12" viewBox="0 0 12 12" fill="none" stroke="#fff" stroke-width="2"><circle cx="5" cy="5" r="3"/><path d="M7.5 7.5l3 3"/></svg></div>
  <div class="abs step-dot" style="left:537px"><svg width="13" height="11" viewBox="0 0 13 11" fill="#fff"><ellipse cx="6.5" cy="5" rx="6" ry="4.3"/><path d="M2 8l-1 3 4-2z"/></svg></div>
  <div class="abs step-dot" style="left:702px"><svg width="10" height="12" viewBox="0 0 10 12" fill="#fff"><path d="M0 0h10v12H0z"/><path d="M2 2h2v2H2zM6 2h2v2H6zM2 6h2v2H2zM6 6h2v2H6z" fill="#e1061a"/></svg></div>
  <div class="abs step-dot" style="left:869px;font-size:13px;font-weight:700;color:#fff">$</div>

  <div class="abs step-card" style="left:198px;height:124px">Artists and venues sign up for free and create a profile</div>
  <div class="abs step-card" style="left:363px;height:124px">Venues search for an artist for their upcoming gigs</div>
  <div class="abs step-card" style="left:529px;height:143px">Venues request a quote and communicate with the artist direct</div>
  <div class="abs step-card" style="left:694px;height:143px">The gig is booked in once payment is provided by the venue.</div>
  <div class="abs step-card" style="left:860px;height:162px">Upon completion the money is paid to the artist within 48 hours or less.</div>
</section>

<section class="why">
  <svg class="abs why-bg" viewBox="0 0 1200 1268" preserveAspectRatio="none" aria-hidden="true"><polygon points="0,0 1188,0 0,1268" fill="var(--red)"/></svg>
  <h2 class="abs why-title">Why TuneNest?</h2>
  <div class="abs why-panel"></div>
  <div class="abs why-core"><div class="brand"><span class="brand-dot"></span>TuneNest</div></div>

  <div class="abs feature right-al" style="left:212px;top:1323px;width:150px"><h3>Connect</h3><p>Join the TuneNest community which is full of amazing artists and venues.</p></div>
  <div class="abs feature-icon" style="left:379px;top:1323px"><svg width="50" height="42" viewBox="0 0 50 42" fill="#fff"><ellipse cx="20" cy="16" rx="18" ry="13"/><path d="M8 25l-4 9 11-6z"/><ellipse cx="33" cy="24" rx="15" ry="11" fill="#fff" stroke="#e1061a" stroke-width="3"/><path d="M42 32l4 8-10-5z"/></svg></div>

  <div class="abs feature-icon" style="left:721px;top:1323px"><svg width="38" height="44" viewBox="0 0 38 44" fill="none" stroke="#fff" stroke-width="4"><path d="M19 3l15 5v12c0 11-7 18-15 21C11 38 4 31 4 20V8z"/><path d="M19 9v27c5-2 9-7 9-15V12z" fill="#fff" stroke="none"/></svg></div>
  <div class="abs feature" style="left:835px;top:1323px;width:185px"><h3>Protection</h3><p style="font-size:14.5px;line-height:23px">Everyone is protected with our complimentary dispute resolutions.</p></div>

  <div class="abs feature right-al" style="left:205px;top:1498px;width:150px"><h3>Simple</h3><p>TuneNest makes gig booking easy for both the venue and artist.</p></div>
  <div class="abs feature-icon" style="left:372px;top:1491px"><svg width="46" height="40" viewBox="0 0 46 40" fill="#fff"><path d="M16 5h28v5H16zM16 18h28v5H16zM16 31h28v5H16z"/><text x="2" y="12" font-size="11" font-family="Montserrat,sans-serif" font-weight="700">1</text><text x="2" y="25" font-size="11" font-family="Montserrat,sans-serif" font-weight="700">2</text><text x="2" y="38" font-size="11" font-family="Montserrat,sans-serif" font-weight="700">3</text></svg></div>

  <div class="abs feature-icon" style="left:731px;top:1489px;font-size:50px;font-weight:700;color:#fff">$</div>
  <div class="abs feature" style="left:844px;top:1487px;width:150px"><h3>Price</h3><p>Get the best rate possible with TuneNest only receiving 5% of the artists fee</p></div>

  <div class="abs venues">
    <h2 class="block-title">Venues</h2>
    <ul class="perks">
      <li>TuneNest is a 100% FREE service for all venues - you pay us nothing!</li>
      <li>Get instant access to hundreds of artists around your local community</li>
      <li>All genres to suit any venue from a pub to a wedding or even a nightclub</li>
      <li>Simple booking process with a money back guarantee</li>
      <li>Communicate directly with the artist and negotiate the price</li>
    </ul>
    <p class="note">TuneNest is not yet ready to host gigs as we're currently working on building our artists. We are launching for venues in Q4 2019. Pre-register now to keep informed and be one of the first people to use our platform.</p>
    <p class="form-lead">Pre-register now to keep informed and be one of the first people to use our platform.</p>
    <form class="signup"><input type="email" placeholder="Email"><button type="button">Pre register</button></form>
  </div>

  <div class="abs artists-card">
    <div class="abs artists">
      <h2 class="block-title">Artists</h2>
      <ul class="perks">
        <li>Sign up to TuneNest for FREE and get yourself in front of venues</li>
        <li>Only pay us if you get a gig - we only get 5% of the fee you charge the venue</li>
        <li>All genres and artists welcome - as long as you're experienced and professional</li>
        <li>Get paid within 48 hours or less after the gig guaranteed!</li>
        <li>Negotiate your price and don't pay huge agent fees to ensure you earn top dollar</li>
      </ul>
      <p class="form-lead">Sign up and create your TuneNest profile now</p>
      <form class="signup"><input type="email" placeholder="Email"><button type="button">Sign up</button></form>
    </div>
  </div>
</section>

<section class="about">
  <div class="abs about-photo" role="img" aria-label="Concert crowd with raised hands in front of an orange-lit stage"></div>
  <div class="abs about-band"></div>
  <h2 class="abs about-title">About TuneNest</h2>
  <div class="abs about-col" style="left:195px">
    <h3>About</h3>
    <p>TuneNest is not yet ready to host gigs as we're currently working on building our artists. We are launching for venues in Q4 2019. Pre-register now to keep informed and be one of the first people to use our platform.</p>
    <p>TuneNest is not yet ready to host gigs as we're currently working on building our artists. We are launching for venues in Q4 2019. Pre-register now to keep informed and be one of the first people to use our platform.</p>
  </div>
  <div class="abs about-col" style="left:639px">
    <h3>About</h3>
    <p>TuneNest is not yet ready to host gigs as we're currently working on building our artists. We are launching for venues in Q4 2019. Pre-register now to keep informed and be one of the first people to use our platform.</p>
    <p>TuneNest is not yet ready to host gigs as we're currently working on building our artists. We are launching for venues in Q4 2019. Pre-register now to keep informed and be one of the first people to use our platform.</p>
  </div>
</section>

<section class="abs contact">
  <h2 class="abs contact-title">Get In touch</h2>
  <input class="abs field" style="left:186px;top:202px;width:382px" placeholder="Name">
  <input class="abs field" style="left:186px;top:245px;width:185px" placeholder="Email">
  <input class="abs field" style="left:382px;top:245px;width:186px" placeholder="Phone">
  <textarea class="abs field" style="left:186px;top:277px;width:382px" placeholder="Message"></textarea>
  <button class="abs send" type="button">Send message</button>

  <div class="abs contact-card">
    <svg class="abs" style="left:210px;top:85px" width="24" height="38" viewBox="0 0 24 38" fill="none" stroke="#666" stroke-width="3"><rect x="2" y="2" width="20" height="34" rx="3"/><path d="M2 28h20" /><circle cx="12" cy="32" r="1.2" fill="#666"/></svg>
    <p class="phone">(555) 014-2290</p>
    <p class="info" style="top:200px"><b>Address</b> 48 Harbor Lane, Milltown, OR, 97001</p>
    <p class="info" style="top:232px"><b>Email</b> hello@tunenest.app</p>
  </div>
</section>

<footer class="abs footer">© 2019 TuneNest</footer>

</body>
</html>
```